BANNER FOR ONLINE CABINET COMPANY MAIN PAGE

Need 3 different banners for the main page. We are online platform for ordering cabinets, parts etc. online.
Website: trimfit.ca
A place where the banner will be placed: https://view.snapvault.example/qR7TpWzKmB4eX
Banner size: 1344x399 pixels
****Clients should get the main point that they can order everything online through the website.

Industry/Entity Type

online cabinets and parts ordering

Requirements
Must have
• online ordering icons, iphone, laptop, desktop pc - so clients get an idea that this is web based service to order cabinets

```html
<!DOCTYPE html>
<html lang="en">
<head>
<meta charset="utf-8">
<title>TrimFit – Custom Cabinets Online</title>
<link rel="stylesheet" href="https://fonts.googleapis.com/css2?family=Arimo:wght@400;500;700&display=swap">
<style>
  :root {
    --bar: #35383c;
    --bar-text: #ffffff;
    --green: #2db34a;
    --band: #e9eaeb;
    --ink: #111111;
    --muted: #5b5b5b;
    --hero-text: #3b332d;
    --button: #4f4640;
    --dot: #d3d3d3;
    --dot-active: #f39c12;
    --numeral: #e3edf8;
    --icon-blue: #2f7fd6;
    --chat: #2c3340;
    --scroll: #dcdcdc;
  }
  * { box-sizing: border-box; margin: 0; padding: 0; }
  html, body { width: 1200px; height: 554px; overflow: hidden; background: #fff; }
  body { position: relative; font-family: "Arimo", Arial, sans-serif; color: var(--ink); }

  .top-bar {
    position: absolute; left: 0; top: 0; width: 1191px; height: 30px;
    background: var(--bar); color: var(--bar-text);
  }
  .brand { position: absolute; left: 27px; top: 8px; font-weight: 700; font-size: 13px; letter-spacing: 0.2px; }
  .brand-divider { position: absolute; left: 99px; top: 6px; width: 1px; height: 18px; background: #fff; }
  .tagline { position: absolute; left: 111px; top: 10px; font-size: 8.5px; }
  .contact-box {
    position: absolute; left: 207px; top: 7px; width: 197px; height: 16px;
    background: #000; font-size: 7px; display: flex; align-items: center; gap: 6px; padding-left: 8px;
  }
  .contact-box svg { flex: none; }
  .nav { position: absolute; top: 0; height: 30px; display: flex; align-items: center; font-size: 7.5px; font-weight: 500; }
  .nav span { position: absolute; white-space: nowrap; }
  .order-pill { background: var(--green); border-radius: 8px; padding: 3px 8px; font-weight: 700; }
  .nav-icon { position: absolute; top: 8px; }

  .scrollbar { position: absolute; left: 1191px; top: 0; width: 9px; height: 554px; background: #f1f1f1; }
  .scrollbar::after { content: ""; position: absolute; left: 2px; top: 2px; width: 5px; height: 85px; background: var(--scroll); border-radius: 3px; }

  .intro-band { position: absolute; left: 0; top: 30px; width: 1191px; height: 57.5px; background: var(--band); text-align: center; }
  .intro-title { margin-top: 5px; font-size: 18.5px; font-weight: 700; letter-spacing: 0.5px; }
  .intro-sub { margin-top: 4px; font-size: 13.7px; color: var(--muted); }

  .hero { position: absolute; left: 0; top: 87.5px; width: 1191px; height: 362.5px; overflow: hidden; }
  .hero-photo {
    position: absolute; inset: 0;
    background: linear-gradient(90deg, #c9c0b5 0%, #b8ab9d 41.6%, #e6e3df 41.7%, #e8e6e2 55%, #6a5a4c 68%, #4b3e34 82%, #3e342c 100%);
  }
  .hero-panel { position: absolute; left: 0; top: 0; width: 496px; height: 100%; background: rgba(185, 170, 155, 0.55); }
  .hero-title {
    position: absolute; left: 64px; top: 79px;
    font-size: 38.5px; line-height: 44px; font-weight: 400; color: var(--hero-text); letter-spacing: 0.3px;
  }
  .hero-sub { position: absolute; left: 64px; top: 190px; font-size: 20px; line-height: 22.5px; color: var(--hero-text); white-space: nowrap; }
  .hero-button {
    position: absolute; left: 64px; top: 275px; width: 297px; height: 37.5px;
    background: var(--button); color: #fff; font-size: 19.3px;
    display: flex; align-items: center; justify-content: center;
  }
  .device-icons { position: absolute; left: 378px; top: 279px; display: flex; align-items: flex-end; gap: 10px; }
  .device-icons svg { display: block; }

  .slide-dots { position: absolute; left: 544px; top: 449px; display: flex; gap: 8px; }
  .slide-dots i { display: block; width: 7px; height: 5px; background: var(--dot); }
  .slide-dots i.active { background: var(--dot-active); }

  .section-title { position: absolute; left: 0; width: 1191px; top: 477px; text-align: center; font-size: 18.5px; font-weight: 700; letter-spacing: 0.4px; }
  .steps { position: absolute; left: 0; top: 525px; width: 1191px; height: 29px; overflow: hidden; }
  .step-num { position: absolute; top: 0; font-size: 70px; font-weight: 700; color: var(--numeral); line-height: 1; }
  .step-icon { position: absolute; top: 16px; width: 14px; height: 14px; border: 1.5px solid var(--icon-blue); border-radius: 2px; }

  .chat-tab {
    position: absolute; left: 1025px; top: 524px; width: 150px; height: 30px;
    background: var(--chat); color: #fff; font-size: 7.5px; border-radius: 4px 4px 0 0; padding: 9px 0 0 9px;
  }
  .chat-tab::after { content: ""; position: absolute; right: -6px; top: 0; width: 14px; height: 14px; border-radius: 50%; background: var(--green); }
</style>
</head>
<body>
  <header class="top-bar">
    <div class="brand">TrimFit</div>
    <div class="brand-divider"></div>
    <div class="tagline">Get the size you need!</div>
    <div class="contact-box">
      <svg width="9" height="9" viewBox="0 0 24 24"><path fill="#fff" d="M6.6 10.8a15 15 0 0 0 6.6 6.6l2.2-2.2c.3-.3.7-.4 1-.2 1.1.4 2.3.6 3.6.6.6 0 1 .4 1 1V20c0 .6-.4 1-1 1A17 17 0 0 1 3 4c0-.6.4-1 1-1h3.5c.6 0 1 .4 1 1 0 1.3.2 2.5.6 3.6.1.3 0 .7-.2 1z"/></svg>
      <span>Call us (555) 014 2290</span>
      <svg width="9" height="9" viewBox="0 0 24 24" style="margin-left:6px"><circle cx="12" cy="12" r="10" fill="none" stroke="#fff" stroke-width="2.5"/><path d="M12 6v6l4 2" fill="none" stroke="#fff" stroke-width="2.5"/></svg>
      <span>Mon-Fri 8AM - 4.30PM</span>
    </div>
    <nav class="nav">
      <span style="left:692px">CAD</span>
      <span class="order-pill" style="left:720px">ORDER NOW</span>
      <span style="left:794px">DESIGN &amp; QUOTE</span>
      <span style="left:867px">SAMPLES</span>
      <span style="left:915px">ABOUT</span>
      <span style="left:953px">CONTACT</span>
      <span style="left:1000px">ARTICLES</span>
    </nav>
    <svg class="nav-icon" style="left:1059px;top:10px" width="10" height="10" viewBox="0 0 24 24"><circle cx="10" cy="10" r="7" fill="none" stroke="#fff" stroke-width="2.5"/><path d="M15 15l6 6" stroke="#fff" stroke-width="2.5"/></svg>
    <svg class="nav-icon" style="left:1096px" width="12" height="14" viewBox="0 0 24 28"><path d="M6 9a6 6 0 1 1 9 5c-2 1-3 2-3 4" fill="none" stroke="#fff" stroke-width="4"/><circle cx="12" cy="25" r="2.5" fill="#fff"/></svg>
    <svg class="nav-icon" style="left:1129px" width="14" height="14" viewBox="0 0 24 24"><circle cx="12" cy="8" r="4.5" fill="none" stroke="#fff" stroke-width="2"/><path d="M3 22c1-5 5-7 9-7s8 2 9 7z" fill="none" stroke="#fff" stroke-width="2"/></svg>
    <svg class="nav-icon" style="left:1164px" width="14" height="13" viewBox="0 0 24 22"><path d="M1 2h4l3 12h12l2-8H7" fill="none" stroke="#fff" stroke-width="2"/><circle cx="9" cy="19" r="1.8" fill="#fff"/><circle cx="18" cy="19" r="1.8" fill="#fff"/></svg>
  </header>

  <section class="intro-band">
    <h1 class="intro-title">THE FIRST ONLINE CUSTOM CABINET’S MANUFACTURER</h1>
    <p class="intro-sub">Order custom cabinets online with instant price calculator. No hidden fees, top quality warranty.</p>
  </section>

  <section class="hero">
    <div class="hero-photo" role="img" aria-label="Modern kitchen with dark wood veneer cabinets, lit open shelving with glass jars, a built-in oven and a white counter"></div>
    <div class="hero-panel"></div>
    <h2 class="hero-title">VENEER DOORS<br>AND FRONTS</h2>
    <p class="hero-sub">Choose from : Walnut Veneer, Maple Veneer,<br>Red Oak Veneer, White Oak Veneer</p>
    <div class="hero-button">GET THE INSTANT PRICE</div>
    <div class="device-icons" aria-label="Order online from phone, laptop or desktop">
      <svg width="16" height="28" viewBox="0 0 16 28"><rect x="1" y="1" width="14" height="26" rx="3" fill="none" stroke="#4f4640" stroke-width="2"/><circle cx="8" cy="23" r="1.3" fill="#4f4640"/></svg>
      <svg width="40" height="26" viewBox="0 0 40 26"><rect x="6" y="1" width="28" height="19" rx="1.5" fill="none" stroke="#4f4640" stroke-width="2"/><path d="M1 23h38" stroke="#4f4640" stroke-width="3" stroke-linecap="round"/></svg>
      <svg width="34" height="30" viewBox="0 0 34 30"><rect x="1" y="1" width="32" height="21" rx="1.5" fill="none" stroke="#4f4640" stroke-width="2"/><path d="M17 22v5M10 28h14" stroke="#4f4640" stroke-width="2" stroke-linecap="round"/></svg>
    </div>
  </section>

  <div class="slide-dots"><i></i><i></i><i></i><i></i><i></i><i class="active"></i><i></i><i></i></div>

  <h2 class="section-title">EASY QUOTE &amp; ORDER</h2>
  <div class="steps">
    <span class="step-num" style="left:258px">1</span><span class="step-icon" style="left:309px"></span>
    <span class="step-num" style="left:425px">2</span><span class="step-icon" style="left:482px"></span>
    <span class="step-num" style="left:597px">3</span><span class="step-icon" style="left:648px"></span>
    <span class="step-num" style="left:783px">4</span><span class="step-icon" style="left:818px"></span>
  </div>

  <div class="chat-tab">Questions? Start chat, we are online!</div>
  <div class="scrollbar"></div>
</body>
</html>
```